IT supplier clean wordpress website - payment guaranteed

Clean website design for a wordpress based website
Design only - PSD delivery with images

current website: www.quorvel.net
please use your imagination and try something out of the box...
We like https://tavrinex.com.au as look and feel, but you don't have to copy it, you can be creative

We like the navigation header and the phone number, but do not need 'instant quote' so the 1300 phone number and the 'lock' icon for login can be on the same line

Site Map:
IT support
VoIP
Internet and Data
Cloud hosting
About
Contact

Our logo is attached, it can be used light or dark.
Our only color used is the warm grey Pantone 8003C hex #877A69

You will only need to design the homepage to win the competition, but the winning designer will be required to supply without extra charges:
1. Home page design
2. A second, standard page template design
3. An icon set in colors appropriate to the site that have icons to match the subjects in these pages:
https://tavrinex.com.au/products/
https://tavrinex.com.au/making-the-switch/
https://tavrinex.com.au/why-tavrinex/
We will create a single page version of the options on https://tavrinex.com.au/solutions/
4.Any images used

Please avoid stock photos that are too common - e.g. smiling woman with headset, try to make the design stand out with simple images and well-designed layout.

Target Market(s)

Mid-size business clients

Industry/Entity Type

It Company

Number of Pages Required

1 page

Requirements
Must have
• Quor logo
• Use Quor color

```html
<!DOCTYPE html>
<html lang="en">
<head>
<meta charset="utf-8">
<title>Quor – Products</title>
<link rel="stylesheet" href="https://fonts.googleapis.com/css2?family=Roboto:wght@400;500;700;900&display=swap">
<style>
:root{
  --brand:#877A69;
  --header:#8a7c6a;
  --accent:#e48a26;
  --ink:#2b2b2b;
  --text:#555;
  --muted:#777;
  --line:#e2e2e2;
  --band:#f1efeb;
  --footer:#21160f;
  --footer-text:#b9ada0;
  --white:#fff;
}
*{box-sizing:border-box;margin:0;padding:0}
html,body{width:1200px;height:2244px;overflow:hidden}
body{position:relative;font-family:'Roboto',Arial,sans-serif;color:var(--text);background:var(--white)}
.abs{position:absolute}

/* Header */
.site-header{left:0;top:0;width:1200px;height:109px;background:var(--header)}
.brand{left:112px;top:36px;display:flex;align-items:center;gap:10px;color:var(--white);font-size:28px;font-weight:500;line-height:34px}
.brand-square{width:16px;height:16px;background:var(--white)}
.main-nav{left:253px;top:42px;display:flex;gap:21px}
.main-nav a{color:var(--white);text-decoration:none;font-size:16px;font-weight:500}
.phone{left:868px;top:41px;color:var(--white);font-size:17px;font-weight:500;display:flex;align-items:center;gap:8px}
.login{left:1002px;top:37px;width:86px;height:34px;background:var(--accent);color:var(--white);font-size:15px;font-weight:700;display:flex;align-items:center;justify-content:center;gap:6px;border-radius:2px}

/* Hero */
.hero{left:0;top:109px;width:1200px;height:373px;background:linear-gradient(90deg,#6f6151 0%,#a39685 35%,#c7b9a4 55%,#8e8a6c 80%,#5f6a4c 100%)}
.hero-frame{left:458px;top:128px;width:337px;height:334px;border:10px solid var(--accent);border-radius:48px}
.hero-title{left:458px;top:262px;width:337px;text-align:center;color:var(--white);font-size:58px;font-weight:900;letter-spacing:-1px}

/* Products */
.product-card{width:308px;height:281px;border:1px solid var(--line);background:var(--white);text-align:center;padding:27px 18px 0}
.product-card svg{display:block;margin:0 auto 22px;width:48px;height:48px}
.product-card h3{font-size:15px;font-weight:500;color:var(--ink);line-height:21px;margin-bottom:14px}
.product-card p{font-size:13px;line-height:21px;color:var(--text)}

/* Enquiry */
.enquiry{left:0;top:1171px;width:1200px;height:636px;background:var(--band)}
.enquiry-title{left:0;top:1219px;width:1200px;text-align:center;font-size:21px;font-weight:500;color:var(--ink);letter-spacing:.3px}
.title-rule{left:540px;top:1263px;width:120px;height:2px;background:linear-gradient(90deg,#555 0 50%,var(--accent) 50% 100%)}
.enquiry-lead{left:0;top:1278px;width:1200px;text-align:center;font-size:16px;line-height:22px;color:var(--text)}
.field{height:44px;background:var(--white);border:1px solid #d8d4cc;border-radius:3px;display:flex;align-items:center;padding-left:14px;gap:8px;font-size:14px;color:#666}
.field svg{width:15px;height:15px}
.field.message{align-items:flex-start;padding-top:13px;height:94px}
.submit{left:467px;top:1656px;width:265px;height:44px;background:var(--accent);border:1px solid #c87418;border-radius:3px;color:var(--white);font-size:17px;font-weight:700;display:flex;align-items:center;justify-content:center}
.privacy{left:0;top:1722px;width:1200px;text-align:center;font-size:13px;line-height:19px;color:#555}

/* Certifications */
.cert{height:60px;width:68px;border-radius:6px}
.cert.one{left:440px;top:1866px;background:#d7d7d3}
.cert.two{left:572px;top:1864px;background:#c9c9c9;border-radius:50%;width:64px;height:64px}
.cert.three{left:696px;top:1862px;background:#1f5d72;height:68px}

/* Footer */
.site-footer{left:0;top:1997px;width:1200px;height:247px;background:var(--footer)}
.footer-col h4{color:var(--white);font-size:15px;font-weight:500;margin-bottom:12px}
.footer-col p,.footer-col li{font-size:12px;line-height:22.5px;color:var(--footer-text);list-style:none}
.remote-dot{width:40px;height:40px;border-radius:50%;background:var(--accent);border:3px solid #f6b25e}
.legal{left:111px;top:2212px;font-size:12px;color:var(--footer-text)}
.social{top:2214px;width:12px;height:12px;border-radius:50%;background:#9c9187}
</style>
</head>
<body>

<header class="abs site-header"></header>
<div class="abs brand"><span class="brand-square"></span>Quor</div>
<nav class="abs main-nav">
  <a href="#">IT support</a><a href="#">VoIP</a><a href="#">Internet and Data</a><a href="#">Cloud hosting</a><a href="#">About</a><a href="#">Contact</a>
</nav>
<div class="abs phone">
  <svg width="12" height="16" viewBox="0 0 12 16"><rect x="1" y="0.5" width="10" height="15" rx="1.5" fill="#fff"/><rect x="3" y="2.5" width="6" height="8" fill="#8a7c6a"/></svg>
  02 5550 1847
</div>
<div class="abs login">
  <svg width="11" height="13" viewBox="0 0 11 13"><path d="M2.5 6V4a3 3 0 0 1 6 0v2" stroke="#fff" stroke-width="1.8" fill="none"/><rect x="0.5" y="6" width="10" height="7" rx="1" fill="#fff"/></svg>
  LOGIN
</div>

<section class="abs hero" role="img" aria-label="Blurred city street photograph with a man carrying an orange cloud"></section>
<div class="abs hero-frame"></div>
<div class="abs hero-title">products</div>

<article class="abs product-card" style="left:112px;top:533px">
  <svg viewBox="0 0 48 48" fill="none" stroke-width="1.6"><rect x="3" y="8" width="26" height="18" stroke="#555"/><rect x="31" y="4" width="12" height="26" stroke="#e48a26"/><path d="M10 32h14M16 26v6" stroke="#555"/><rect x="6" y="36" width="22" height="6" stroke="#555"/><rect x="34" y="34" width="6" height="9" rx="3" stroke="#e48a26"/></svg>
  <h3>Corporate<br>Workstations</h3>
  <p>Robust, business grade performance and reliability. Why choose any other PC when you can afford Veltra.</p>
</article>
<article class="abs product-card" style="left:446px;top:533px">
  <svg viewBox="0 0 48 48" fill="none" stroke-width="1.6"><rect x="4" y="6" width="32" height="24" stroke="#555"/><path d="M14 38h12M20 30v8" stroke="#555"/><rect x="32" y="20" width="12" height="20" rx="2" stroke="#e48a26"/></svg>
  <h3>OrbiDesk, OrbiBook,<br>OrbiTab &amp; OrbiPhone</h3>
  <p>Great for home and the kids. Sleek, stylish and capable. You can easily integrate with your business systems if you have the Quor advantage. Use tablets and phones with RDP, Mailhub and custom apps.</p>
</article>
<article class="abs product-card" style="left:779px;top:533px">
  <svg viewBox="0 0 48 48" fill="none" stroke-width="1.6"><rect x="6" y="4" width="36" height="12" rx="1" stroke="#555"/><rect x="6" y="18" width="36" height="12" rx="1" stroke="#555"/><rect x="6" y="32" width="36" height="12" rx="1" stroke="#555"/><path d="M12 10h8M12 24h8M12 38h8" stroke="#e48a26"/></svg>
  <h3>Veltra Standalone &amp;<br>Blade Servers</h3>
  <p>The only serious choice in servers. multiple distributed and redundant systems. Cross-platform integration. 24x7 support. Virtualisation and cloud computing at its best.</p>
</article>
<article class="abs product-card" style="left:112px;top:839px">
  <svg viewBox="0 0 48 48" fill="none" stroke-width="1.6"><rect x="12" y="4" width="24" height="12" stroke="#e48a26"/><rect x="4" y="16" width="40" height="18" rx="2" stroke="#555"/><rect x="12" y="28" width="24" height="14" stroke="#555"/><path d="M16 34h16M16 38h12" stroke="#e48a26"/></svg>
  <h3>Veltra &amp; Norvik<br>Printers</h3>
  <p>Buy right, buy once. Don't muck around with incessant inkjet refills and lower quality devices. Get the results you want, every time.</p>
</article>
<article class="abs product-card" style="left:446px;top:839px">
  <svg viewBox="0 0 48 48" fill="none" stroke-width="1.6"><path d="M10 22a14 14 0 0 1 28 0z" stroke="#555"/><path d="M8 22h32" stroke="#555"/><path d="M24 8v6" stroke="#e48a26"/><path d="M8 44l6-12M40 44l-6-12M14 40h20" stroke="#e48a26"/></svg>
  <h3>Maintenance<br>Contracts</h3>
  <p>Scheduled maintenance and SLA's to keep your machines doing their job. Reduce downtime costs. Self-diagnostics and remote monitoring. Get the total package.</p>
</article>

<section class="abs enquiry"></section>
<h2 class="abs enquiry-title">FIND OUT HOW TAVRINEX CAN HELP</h2>
<div class="abs title-rule"></div>
<p class="abs enquiry-lead">Spend less time managing your IT systems with a tailored, all in one<br>solution - and free up more time to concentrate on your business.</p>

<div class="abs field" style="left:278px;top:1363px;width:308px"><svg viewBox="0 0 16 16" fill="none" stroke="#888"><circle cx="8" cy="5" r="3.5"/><path d="M1.5 15a6.5 6.5 0 0 1 13 0"/></svg>First Name*</div>
<div class="abs field" style="left:613px;top:1363px;width:308px"><svg viewBox="0 0 16 16" fill="none" stroke="#888"><rect x="1" y="4" width="14" height="10" rx="1"/><path d="M5 4V2h6v2"/></svg>Last Name*</div>
<div class="abs field" style="left:278px;top:1420px;width:308px"><svg viewBox="0 0 16 16" fill="none" stroke="#888"><rect x="1" y="3" width="14" height="10"/><path d="M1 3l7 6 7-6"/></svg>Email*</div>
<div class="abs field" style="left:613px;top:1420px;width:308px"><svg viewBox="0 0 16 16" fill="none" stroke="#888"><rect x="4" y="1" width="8" height="14" rx="1.5"/><path d="M7 12.5h2"/></svg>Phone*</div>
<div class="abs field" style="left:278px;top:1477px;width:643px"><svg viewBox="0 0 16 16" fill="none" stroke="#888"><rect x="2" y="1" width="12" height="14"/><path d="M5 4h2M9 4h2M5 7h2M9 7h2M5 10h2M9 10h2"/></svg>Company Name*</div>
<div class="abs field message" style="left:278px;top:1535px;width:643px"><svg viewBox="0 0 16 16" fill="none" stroke="#888"><circle cx="8" cy="5" r="3.5"/><path d="M2 15a6 6 0 0 1 12 0"/></svg>How can we help you?</div>
<div class="abs submit">FIND OUT MORE</div>
<p class="abs privacy">We guarantee 100% privacy.<br>Your information will not be shared.</p>

<div class="abs cert one" aria-label="Certification badge"></div>
<div class="abs cert two" aria-label="Certification badge"></div>
<div class="abs cert three" aria-label="Certification badge"></div>

<footer class="abs site-footer"></footer>
<div class="abs footer-col" style="left:111px;top:2046px;width:215px">
  <h4>About Company</h4>
  <p>Servicing industry's IT needs with experience in extensive technologies and platforms with a focus on customer service.</p>
</div>
<div class="abs footer-col" style="left:443px;top:2046px">
  <h4>Our Services</h4>
  <ul><li>Hardware Software Support</li><li>Data and Voice</li><li>Cloud Services</li><li>Support</li></ul>
</div>
<div class="abs footer-col" style="left:696px;top:2046px">
  <h4>Products</h4>
  <ul><li>Corporate Workstations</li><li>OrbiDesk, OrbiBook, OrbiTab and OrbiPhone</li><li>Veltra Standalone and Blade Servers</li><li>Veltra and Norvik Printers</li></ul>
</div>
<div class="abs footer-col" style="left:945px;top:2046px">
  <h4>Remote</h4>
</div>
<div class="abs remote-dot" style="left:946px;top:2076px"></div>
<div class="abs remote-dot" style="left:996px;top:2076px"></div>
<p class="abs legal">© 2017Quor. Terms of Use &nbsp;|&nbsp; Privacy &nbsp;|&nbsp; Sitemap</p>
<div class="abs social" style="left:1050px"></div>
<div class="abs social" style="left:1072px"></div>

</body>
</html>
```